Wine and retail website for a high-end resort community

We are introducing a line of quality wines in the resort community of Gull Point, Massachusetts, USA. The site will detail information about the wine, and online store connected to and external government approved shipper for wine, and additional non-alcoholic retail merchandise sales.

We are planning the site to be driven off the Squarespace platform so I do not believe coding is necessary initially; however, the ability to do sop would be helpful if needed.

Attached are the images/files we have available so far. Please feel free to use stock images in your design.

Target Market(s)

Wine enthusiasts in the resort community of Martha’s Vineyard Massachusetts

Industry/Entity Type

Wine

Number of Pages Required

4 page

Font styles to use
Sans Serif

Requirements
Must have
• Home page, about page, wine page, e-commerce page, retail merchandise page. I recently came across brelmorcellars.com and really like the look and layout of their pages if that helps
Nice to have
• A short wine/Martha’s Vineyard related video on the home page

```html
<!DOCTYPE html>
<html lang="en">
<head>
<meta charset="utf-8">
<title>Gull Point Estates</title>
<link href="https://fonts.googleapis.com/css2?family=Playfair+Display:ital,wght@0,400;0,700;1,400&family=Lato:wght@300;400;700&display=swap" rel="stylesheet">
<style>
:root{
  --maroon:#6b2c37;
  --gold:#c9b23b;
  --ink:#1f1a1b;
  --footer:#2b2122;
  --grey:#8b8b8b;
  --line:#cfc6c6;
  --white:#ffffff;
}
*{box-sizing:border-box;margin:0;padding:0}
html,body{width:1200px;height:3998px;overflow:hidden;background:var(--white)}
body{position:relative;font-family:'Lato',sans-serif;color:var(--ink)}
.abs{position:absolute}

/* header */
.social{top:76px;left:28px;display:flex;gap:28px}
.social span{width:16px;height:16px;border-radius:50%;background:var(--ink);display:block}
.brand{top:40px;left:0;width:1200px;text-align:center;font-family:'Playfair Display',serif;font-size:30px;line-height:30px;color:var(--ink);letter-spacing:1px}
.brand small{display:block;font-size:12px;line-height:20px;letter-spacing:5px}
.tools{top:66px;right:44px;display:flex;gap:22px}
.nav{top:136px;left:0;width:1200px;height:58px;background:var(--maroon);font-family:'Playfair Display',serif;font-variant:small-caps;font-size:19px}
.nav a{position:absolute;top:16px;color:var(--gold);text-decoration:none;letter-spacing:1px}
.nav a.nav-home{color:var(--white);font-weight:700}

/* hero */
.hero{top:194px;left:0;width:1200px;height:700px;background:linear-gradient(180deg,#3a3536 0%,#2a2526 45%,#1b1717 100%)}
.hero-bottles{top:230px;left:618px;width:232px;height:476px;background:linear-gradient(90deg,#3a1a20 0%,#5a2c33 40%,#c9b56a 70%,#e8dca0 100%);border-radius:30px 30px 6px 6px;opacity:.85}
.hero-kicker{top:322px;left:0;width:600px;text-align:center;color:var(--white);font-family:'Playfair Display',serif;font-weight:700;font-size:26px}
.hero-title{top:352px;left:0;width:600px;text-align:center;color:var(--gold);font-family:'Playfair Display',serif;font-weight:400;font-size:68px;line-height:64px}
.hero-text{top:504px;left:0;width:600px;text-align:center;color:#e6e2e2;font-size:16px;line-height:28px;font-weight:300}
.btn{display:flex;align-items:center;justify-content:center;font-size:19px;text-decoration:none}
.hero-btn{top:582px;left:199px;width:180px;height:56px;background:var(--maroon);color:var(--white);border-radius:3px}
.curve{top:780px;left:0}

.card{top:730px;width:298px;height:297px}
.card-img{position:absolute;inset:0}
.card-copy{position:absolute;left:26px;bottom:12px;color:var(--white)}
.card-copy h3{font-family:'Playfair Display',serif;font-style:italic;font-weight:400;font-size:20px;margin-bottom:8px}
.card-copy p{font-style:italic;font-size:12px;line-height:18px;width:200px}

/* welcome */
.welcome{top:1112px;left:0;width:1200px;text-align:center;font-family:'Playfair Display',serif;font-weight:400;color:var(--maroon);font-size:56px}
.rule{left:326px;width:593px;height:1px;background:var(--line)}
.welcome-text{top:1216px;left:0;width:1200px;text-align:center;color:var(--grey);font-weight:300;font-size:20px;line-height:25px}

/* wine blocks */
.wine-title{font-family:'Playfair Display',serif;font-weight:400;color:var(--maroon);font-size:36px;left:57px}
.wine-region{font-family:'Playfair Display',serif;font-size:24px;left:57px}
.wine-body{left:57px;width:563px;font-size:12.5px;line-height:17px}
.cheers{left:57px;font-size:13px}
.signature{left:57px;width:255px;height:66px;background:linear-gradient(90deg,#e9e6e6,#f6f4f4)}
.label{border:2px solid #d9d5d5;background:linear-gradient(180deg,#ffffff 0%,#f5f3f3 55%,#dedada 100%)}
.isle{top:1336px;left:57px;width:104px;height:52px;background:var(--ink);border-radius:40% 60% 45% 55%}

/* current release */
.release{top:1802px;left:45px;width:1110px;height:601px;background:var(--maroon)}
.release-photo{position:absolute;top:0;left:0;width:562px;height:601px;background:linear-gradient(135deg,#2a1416 0%,#6c3a3f 35%,#efe9de 55%,#c9ac52 80%,#3a2a18 100%)}
.release .txt{position:absolute;color:var(--white)}
.release .year{left:616px;top:56px;font-family:'Playfair Display',serif;font-size:42px;line-height:48px}
.release .release-label{left:616px;top:106px;font-family:'Playfair Display',serif;font-size:20px}
.release .r-name{left:612px;font-family:'Playfair Display',serif;font-size:36px;color:var(--gold)}
.release .r-body{left:612px;width:470px;font-size:12.5px;line-height:17px}
.release .r-btn{top:472px;width:178px;height:49px;font-size:19px}
.release .r-discover{left:612px;background:var(--gold);color:var(--ink)}
.release .r-view{left:804px;border:2px solid var(--gold);color:var(--white)}

/* tasting */
.tasting{top:2907px;left:45px;width:562px;height:607px;background:var(--maroon);color:var(--white);text-align:center}
.tasting-photo{top:2907px;left:607px;width:548px;height:607px;background:radial-gradient(circle at 60% 55%,#8e1a22 0%,#b9522c 30%,#e9c98d 60%,#f5ead6 100%)}
.eyebrow{font-weight:700;font-size:14px;letter-spacing:.5px}
.t-title{font-family:'Playfair Display',serif;font-size:38px}
.t-body{font-size:14px;line-height:28px}
.t-btn{left:189px;top:427px;width:179px;height:47px;background:var(--gold);color:var(--ink)}

/* club */
.club-eye{top:3565px;left:0;width:1200px;text-align:center;font-weight:700;font-size:14px}
.club-title{top:3592px;left:0;width:1200px;text-align:center;font-family:'Playfair Display',serif;font-weight:400;font-size:36px}
.signup{top:3644px;left:45px;width:1110px;height:65px;border:1px solid #ece8e8}
.signup .ph{position:absolute;left:27px;top:25px;font-size:12px;color:#b5b0b0}
.signup .go{position:absolute;right:32px;top:24px;font-size:13px;border-left:1px solid #ece8e8;padding-left:52px}

/* footer */
.footer{top:3765px;left:0;width:1200px;height:233px;background:var(--footer);color:var(--white)}
.footer .f{position:absolute}
.promise{top:34px;left:0;width:1200px;text-align:center;font-weight:700;font-size:14px}
.make{top:68px;left:0;width:1200px;text-align:center;font-family:'Playfair Display',serif;font-variant:small-caps;font-size:34px;letter-spacing:1px}
.f-links{top:158px;font-size:12px}
.f-social{top:157px;left:525px;display:flex;gap:30px}
.f-social span{width:16px;height:16px;border-radius:50%;background:var(--white);display:block}
.copy{top:158px;right:44px;font-size:12px}
</style>
</head>
<body>

<header>
  <div class="abs social"><span></span><span></span><span></span><span></span></div>
  <div class="abs brand">GULL POINT<small>ESTATES</small></div>
  <div class="abs tools">
    <svg width="20" height="20" viewBox="0 0 20 20" fill="none" stroke="#1f1a1b" stroke-width="2"><circle cx="8" cy="8" r="6"/><path d="M13 13l5 5"/></svg>
    <svg width="20" height="20" viewBox="0 0 20 20" fill="none" stroke="#1f1a1b" stroke-width="2"><circle cx="10" cy="6" r="4"/><path d="M3 19c0-5 14-5 14 0"/></svg>
    <svg width="22" height="20" viewBox="0 0 22 20" fill="none" stroke="#1f1a1b" stroke-width="2"><path d="M1 2h4l3 11h11l2-8H6"/><circle cx="9" cy="17" r="1.5"/><circle cx="18" cy="17" r="1.5"/></svg>
  </div>
  <nav class="abs nav">
    <a class="nav-home" href="#" style="left:406px">Home</a>
    <a href="#" style="left:524px">About</a>
    <a href="#" style="left:624px">Shop</a>
    <a href="#" style="left:730px">Contact</a>
  </nav>
</header>

<section>
  <div class="abs hero" role="img" aria-label="Night coastal landscape with a lighthouse and estate houses under a cloudy sky"></div>
  <div class="abs hero-bottles" role="img" aria-label="Bottles of Gull Point Estates Cabernet Sauvignon and Chardonnay"></div>
  <div class="abs hero-kicker">TASTE OUR WINES</div>
  <h1 class="abs hero-title">Discover in<br>Our Wines</h1>
  <p class="abs hero-text">Everyone will find something very own in our<br>outstanding wines. Don't miss the chance.</p>
  <a class="abs btn hero-btn" href="#">Discover</a>
  <svg class="abs curve" width="1200" height="120" viewBox="0 0 1200 120"><path d="M0 70 Q600 -20 1200 70 L1200 120 L0 120 Z" fill="#ffffff"/></svg>

  <article class="abs card" style="left:116px">
    <div class="card-img" role="img" aria-label="Coastal cliffs with a lighthouse under a blue sky" style="background:linear-gradient(180deg,#c5d4df 0%,#9db0b8 40%,#6f7a58 70%,#4b4f36 100%)"></div>
    <div class="card-copy"><h3>Our Story</h3><p>Gull Point Estates Cabernet Sauvignon shows aromas of</p></div>
  </article>
  <article class="abs card" style="left:450px">
    <div class="card-img" role="img" aria-label="Two glasses of red wine raised in a toast at a candlelit table" style="background:linear-gradient(180deg,#1a1414 0%,#3c2522 50%,#6b3a2c 100%)"></div>
    <div class="card-copy"><h3>Make a Reservation</h3><p>Gull Point Estates Cabernet Sauvignon shows aromas of</p></div>
  </article>
  <article class="abs card" style="left:785px">
    <div class="card-img" role="img" aria-label="Wine glasses on a set table with roses" style="background:linear-gradient(180deg,#24302e 0%,#4e5b58 45%,#2a2222 100%)"></div>
    <div class="card-copy"><h3>Join Our Wine Club</h3><p>Gull Point Estates Cabernet Sauvignon shows aromas of</p></div>
  </article>
</section>

<section>
  <h2 class="abs welcome">Welcome to Gull Point Vineyards &amp; Winery</h2>
  <div class="abs rule" style="top:1192px"></div>
  <p class="abs welcome-text">Passionate curiosity started this journey. Tireless effort got us here. A sense of<br>awe keeps us humble. Gratitude makes it real.</p>
  <div class="abs rule" style="top:1285px"></div>
</section>

<section>
  <div class="abs isle" role="img" aria-label="Island silhouette"></div>
  <h3 class="abs wine-title" style="top:1424px">Cabernet Sauvignon</h3>
  <div class="abs wine-region" style="top:1476px">California</div>
  <p class="abs wine-body" style="top:1518px;text-align:justify">Gull Point Estates Cabernet Sauvignon shows aromas of oak, baking spice, and cassis. On the palate, tones of black cherry and a hint of cinnamon, nutmeg and French Vanilla leave a delicious lasting finish.</p>
  <p class="abs wine-body" style="top:1598px">We hope our wines are a reminder of good times and good company spent on the island. Here's to keeping it on island time!</p>
  <div class="abs cheers" style="top:1670px">Cheers,</div>
  <div class="abs signature" style="top:1700px" role="img" aria-label="Handwritten vintner signature"></div>
  <div class="abs label" style="top:1372px;left:695px;width:329px;height:369px" role="img" aria-label="Gull Point Estates Cabernet Sauvignon 2022 wine label with coastal sketch"></div>
</section>

<section class="abs release">
  <div class="release-photo" role="img" aria-label="Close-up of 2022 Cabernet Sauvignon and Chardonnay bottles"></div>
  <div class="txt year">2022</div>
  <div class="txt release-label">CURRENT RELEASE</div>
  <div class="txt r-name" style="top:140px">Cabernet Sauvignon</div>
  <p class="txt r-body" style="top:198px">Gull Point Estates Cabernet Sauvignon shows aromas of oak, baking spice, and cassis. On the palate, tones of black cherry and a hint of cinnamon, nutmeg and French Vanilla leave a delicious lasting finish.</p>
  <div class="txt r-name" style="top:280px">Chardonnay</div>
  <p class="txt r-body" style="top:338px">Gull Point Estates Chardonnay is defined by an array of fragrant fruit with buttery undertones that finish long and smooth. A true classic that is sure to please any palate.</p>
  <a class="txt btn r-btn r-discover" href="#">Discover</a>
  <a class="txt btn r-btn r-view" href="#">View All</a>
</section>

<section>
  <h3 class="abs wine-title" style="top:2468px">Chardonnay</h3>
  <div class="abs wine-region" style="top:2514px">California</div>
  <p class="abs wine-body" style="top:2580px;width:560px">Gull Point Estates Chardonnay is defined by an array of fragrant fruit with buttery undertones that finish long and smooth. A true classic that is sure to please any palate.</p>
  <p class="abs wine-body" style="top:2643px;width:540px">We hope our wines are a reminder of good times and good company spent on the island. Here's to keeping it on island time!</p>
  <div class="abs cheers" style="top:2755px;font-weight:700;font-size:16px">Cheers,</div>
  <div class="abs signature" style="top:2787px" role="img" aria-label="Handwritten vintner signature"></div>
  <div class="abs label" style="top:2493px;left:692px;width:328px;height:321px" role="img" aria-label="Gull Point Estates Chardonnay 2022 wine label with coastal sketch"></div>
</section>

<section>
  <div class="abs tasting">
    <div class="abs eyebrow" style="top:132px;width:562px">THE ESTATE</div>
    <div class="abs t-title" style="top:164px;width:562px">Tasting &amp; Tours</div>
    <p class="abs t-body" style="top:248px;left:90px;width:382px">Lorem ipsum dolor sit amet, consectetur adipiscing. Cras vel iaculis urna. Cras bibendum ex id dolor facilisis, in tempor lacus dapibus.</p>
    <a class="abs btn t-btn" href="#">Read More</a>
  </div>
  <div class="abs tasting-photo" role="img" aria-label="Red wine being poured from a bottle into a glass"></div>
</section>

<section>
  <div class="abs club-eye">BE CONNECTED</div>
  <h2 class="abs club-title">Join Our Club</h2>
  <div class="abs signup"><span class="ph">Email Address</span><span class="go">Sign Up</span></div>
</section>

<footer class="abs footer">
  <div class="f promise">GULL POINT PROMISE</div>
  <div class="f make">We Make Good Wines</div>
  <div class="f f-links" style="left:42px">FAQ</div>
  <div class="f f-links" style="left:104px">TERMS</div>
  <div class="f f-links" style="left:191px">PRIVACY</div>
  <div class="f f-links" style="left:289px">RETURNS</div>
  <div class="f f-social"><span></span><span></span><span></span><span></span></div>
  <div class="f copy">© 2024 GULL POINT . ALL RIGHTS RESERVED</div>
</footer>

</body>
</html>
```